Strategy and Technology Consulting - Our Story and Values Page

Interior Page design – Our History and Our Values

Our homepage has been designed and we are looking for a design for one of the interior pages. This interior page tells the story of Our History and Our Values

Because the homepage has been designed, we would like this interior page to reflect the design of the homepage without being a mirror image of the homepage.

This site will be implemented in WordPress using the Elementor framework.

Font: Poppins medium and Poppins dark
Illustrations: Our homepage illustrations were designed by “Teslo 1964” on Imagevale. Compatible original or stock illustrations are welcome. Stock photography is also welcome. Teslo is also available through Teslo Bramen on Portvue

• Homepage design – this is the design we will use for our homepage. Contest entries should reflect this basic style but should be distinctly different from the homepage.
• Our History and Our Values – Wireframe – the basic layout of the page we are looking for.
• Our History and Our Values – Word document with the text supporting the wireframe.
• Color Palette – please use colors compatible with the palette attached.

Our Story - timeline
There is a timeline element in the wireframe. The wireframe displays this as a series of chevrons (arrows), but it does not need to be. Creativity in display of the timeline is appreciated.

Our Values
If you look at the Word document, you will see that there are a lot of words on the page. The winning design will present the information in a way that engages the user without overwhelming them with too much to read. For example, they may click on a value and see more information.

Target Market(s)

CIO's and Technology Executives

Number of Pages Required

1 page

Font styles to use
Sans Serif
Other font styles liked:
• Poppin

Requirements
Must have
• A timeline element, all of our values
Nice to have
• Clever timeline display

```html
<!DOCTYPE html>
<html lang="en">
<head>
<meta charset="utf-8">
<title>Altivon – Our Story and Values</title>
<link rel="stylesheet" href="https://fonts.googleapis.com/css2?family=Poppins:wght@400;500;600;700;800&display=swap">
<style>
:root{
  --board:#1b4670;
  --hero:#2f6a99;
  --hero-deep:#2a6191;
  --yellow:#e2b913;
  --yellow-soft:#f0c12a;
  --steel:#a8bac7;
  --sky:#bcdcf0;
  --ink:#23374d;
  --muted:#8ea4b8;
  --text:#4a5566;
  --white:#ffffff;
  --footer:#4b5b70;
  --footer-deep:#3e4c60;
  --icon-box:#c5d0d9;
}
*{margin:0;padding:0;box-sizing:border-box}
html,body{width:906px;height:1200px;overflow:hidden}
body{background:var(--board);font-family:"Poppins",sans-serif;position:relative;color:var(--ink)}
.abs{position:absolute}

/* ---------- full page ---------- */
.page{position:absolute;left:40px;top:36px;width:324px;height:1131px;background:var(--white);overflow:hidden}
.site-header{position:absolute;left:0;top:0;width:324px;height:25px;background:var(--white);display:flex;align-items:center}
.brand{position:absolute;left:25px;top:5px;font-size:13px;font-weight:400;color:var(--muted);letter-spacing:.2px;line-height:14px}
.nav{position:absolute;left:146px;top:9px;display:flex;gap:6px;font-size:3.4px;font-weight:600;color:var(--ink);align-items:center}
.nav .home{width:4px;height:4px;background:var(--muted);clip-path:polygon(50% 0,100% 50%,85% 50%,85% 100%,15% 100%,15% 50%,0 50%)}
.nav-cta{position:absolute;left:265px;top:7px;width:35px;height:11px;border-radius:6px;background:var(--yellow);color:var(--white);font-size:3.2px;font-weight:700;display:flex;align-items:center;justify-content:center}

.hero{position:absolute;left:0;top:25px;width:324px;height:240px;background:var(--hero);overflow:hidden}
.skyline{position:absolute;left:0;bottom:0;width:100%;height:150px;background:linear-gradient(180deg,rgba(40,92,136,0) 0%,rgba(38,88,132,.55) 45%,rgba(36,84,128,.7) 100%)}
.hero-wave{position:absolute;left:0;top:185px}

.chev{position:absolute;left:0;display:flex;align-items:center;color:var(--white);font-weight:400}
.chev .flag{display:inline-block;width:4px;height:4px;margin-right:3px;background:var(--white);clip-path:polygon(0 0,100% 0,80% 40%,100% 80%,15% 80%,15% 100%,0 100%)}
.chev.is-yellow{background:var(--yellow)}
.chev.is-steel{background:var(--steel)}
.chev.is-sky{background:var(--sky)}
.chev.is-active{font-weight:800}

.page .chev{height:20.6px;width:109px;padding-left:23px;font-size:6px}
.page .chev.is-active{width:140px;font-size:7.5px;clip-path:polygon(0 0,131px 0,140px 50%,131px 100%,0 100%)}

.tl-title{position:absolute;font-weight:800;color:var(--white);line-height:1}
.tl-item{position:absolute;display:flex;align-items:center;color:var(--white)}
.tl-icon{flex:none;border-radius:2px;display:flex;align-items:center;justify-content:center}
.tl-icon i{display:block;border:1px solid var(--white);border-radius:50%}
.tl-line{position:absolute;border-left:1px dashed rgba(255,255,255,.7)}
.vertical{position:absolute;writing-mode:vertical-rl;font-weight:800;line-height:1}

.page .tl-title{left:183px;top:49px;font-size:13px}
.page .tl-icon{width:17px;height:17px;background:var(--yellow)}
.page .tl-icon i{width:7px;height:7px}
.page .tl-item{left:183px;font-size:6px;line-height:1.3;gap:5px}
.page .vertical{left:307px;top:75px;font-size:12.5px;color:var(--sky);opacity:.9}

/* ---------- values ---------- */
.values-title{position:absolute;left:0;width:324px;top:255px;text-align:center;font-size:12px;font-weight:800;color:var(--muted)}
.value-art{position:absolute;border-radius:40% 40% 10px 10px;background:radial-gradient(ellipse at 50% 45%,#e8b921 0%,#9fb8cc 45%,#e9eff6 80%)}
.value-art.is-blue{background:radial-gradient(ellipse at 50% 50%,#2f6a99 0%,#a8c0d4 50%,#eef3f8 85%)}
.value-art.is-light{background:radial-gradient(ellipse at 50% 50%,#f0c12a 0%,#c9d8e6 55%,#f2f6fa 85%)}
.value{position:absolute;width:116px}
.value h3{font-size:6px;font-weight:800;color:var(--ink);margin-bottom:3px;line-height:1.2}
.value p{font-size:3.7px;line-height:1.55;color:var(--text)}

/* ---------- newsletter & footer ---------- */
.footer{position:absolute;left:0;top:960px;width:324px;height:171px;background:linear-gradient(180deg,var(--footer) 0%,var(--footer-deep) 100%)}
.footer-wave{position:absolute;left:0;top:960px}
.newsletter{position:absolute;left:37px;top:939px;width:249px;height:56px;border-radius:28px;background:linear-gradient(90deg,var(--yellow) 0%,var(--yellow-soft) 100%)}
.newsletter h4{position:absolute;left:22px;top:15px;font-size:8px;font-weight:800;color:var(--white)}
.newsletter p{position:absolute;left:22px;top:28px;font-size:3.7px;line-height:1.4;color:var(--white);font-weight:500}
.email-field{position:absolute;left:149px;top:22px;width:87px;height:13px;border-radius:7px;background:var(--white);font-size:3.3px;color:#9aa6b4;display:flex;align-items:center;padding-left:12px}
.email-field .send{position:absolute;right:1.5px;top:1.5px;width:10px;height:10px;border-radius:50%;background:var(--muted)}
.footer-brand{position:absolute;left:33px;top:1043px;font-size:17px;color:var(--white);opacity:.92;line-height:1}
.socials{position:absolute;left:48px;top:1065px;display:flex;gap:3.5px}
.socials span{width:10px;height:10px;border-radius:50%;background:rgba(255,255,255,.25)}
.footer-cta{position:absolute;left:58px;top:1082px;width:35px;height:11px;border-radius:6px;background:var(--yellow);color:var(--white);font-size:3.2px;font-weight:700;display:flex;align-items:center;justify-content:center}
.f-col{position:absolute;top:1038px;color:var(--white)}
.f-col h5{font-size:5px;font-weight:800;margin-bottom:4px}
.f-col li{list-style:none;font-size:3.4px;line-height:8.4px;opacity:.9}
.f-col li::before{content:"› "}
.contact-row{font-size:3.3px;line-height:1.4;margin-bottom:4px;opacity:.9;padding-left:6px;position:relative}
.contact-row::before{content:"";position:absolute;left:0;top:1px;width:3px;height:3px;border-radius:50%;background:var(--yellow)}
.copyright{position:absolute;left:0;top:1115px;width:324px;height:16px;background:#3d4658;color:var(--white);font-size:3.4px;display:flex;align-items:center;justify-content:center}
.chat{position:absolute;left:306px;top:1108px;width:13px;height:13px;border-radius:50%;background:var(--yellow);border:1.5px solid var(--white)}

/* ---------- timeline panels ---------- */
.panel{position:absolute;left:403px;width:461px;height:229px;background:var(--hero);overflow:hidden}
.panel .skyline{height:130px}
.panel .chev{height:29.5px;width:155px;padding-left:33px;font-size:9px}
.panel .chev .flag{width:6px;height:6px;margin-right:5px}
.panel .chev.is-active{width:200px;font-size:11px;clip-path:polygon(0 0,185px 0,200px 50%,185px 100%,0 100%)}
.panel .tl-title{font-size:17px}
.panel .tl-icon{width:24px;height:24px;background:var(--icon-box)}
.panel .tl-icon i{width:11px;height:11px}
.panel .tl-item{font-size:8.7px;line-height:1.5;gap:8px;font-weight:400}
.panel .vertical{font-size:16px;color:var(--icon-box)}
.bullets{position:absolute;font-size:8.7px;color:var(--white);line-height:13px}
.bullets li{list-style:none;padding-left:8px;position:relative}
.bullets li::before{content:"";position:absolute;left:0;top:5.5px;width:3px;height:3px;border-radius:50%;background:var(--white)}
</style>
</head>
<body>

<main class="page">
  <header class="site-header">
    <div class="brand">Altivon</div>
    <nav class="nav"><span class="home"></span><span>ABOUT US ˅</span><span>SERVICES ˅</span><span>INSIGHTS ˅</span><span>JOIN US ˅</span></nav>
    <div class="nav-cta">CONTACT US</div>
  </header>

  <section class="hero">
    <div class="skyline" role="img" aria-label="Faint city skyline illustration"></div>
    <div class="chev is-yellow is-active" style="top:26px"><span class="flag"></span>2017 – 2019</div>
    <div class="chev is-steel" style="top:46.6px"><span class="flag"></span>2020 - 2021</div>
    <div class="chev is-sky" style="top:67.2px"><span class="flag"></span>2022 and Onward</div>

    <h2 class="tl-title" style="top:24px">2017 – 2019</h2>
    <div class="tl-line" style="left:191px;top:53px;height:78px"></div>
    <div class="tl-item" style="top:45px"><span class="tl-icon"><i></i></span>Growth Strategy Focus</div>
    <div class="tl-item" style="top:70.5px"><span class="tl-icon"><i></i></span>Consistent, Modest Growth</div>
    <div class="tl-item" style="top:95px"><span class="tl-icon"><i></i></span>Preliminary Focus on<br>Technology</div>
    <div class="tl-item" style="top:121px"><span class="tl-icon"><i></i></span><span><b>Eureka!</b> Implementing<br>strategy is hard</span></div>
    <div class="vertical" style="top:52px">Our Story</div>

    <svg class="hero-wave" width="324" height="56" viewBox="0 0 324 56" aria-hidden="true">
      <path d="M0 56 C40 20 100 30 160 30 C220 30 270 0 324 14 L324 56 Z" fill="#ffffff"/>
      <path d="M55 26 C110 44 180 36 230 18 C270 4 300 2 324 10" fill="none" stroke="#bcdcf0" stroke-width="3"/>
    </svg>
  </section>

  <h2 class="values-title">Our Values</h2>

  <div class="value-art" style="left:36px;top:285px;width:116px;height:66px" role="img" aria-label="Illustration of a diverse group of people"></div>
  <div class="value" style="left:178px;top:292px">
    <h3>The Value of Every Human.<br>Regardless.</h3>
    <p>Each person's unique experiences and perspectives add vibrant hues to the tapestry of our shared existence. In a world where diversity paints the canvas of humanity, true beauty is found in recognizing the inherent and incalculable value of every human being.</p>
  </div>

  <div class="value" style="left:37px;top:385px">
    <h3>Collaboration</h3>
    <p>Collaboration in work transforms individual endeavors into symphonies of collective achievement. Through collaboration, diverse talents converge, fostering a rich exchange of ideas that amplifies creativity, accelerates progress, and brings forth solutions beyond what a single mind could conceive.</p>
  </div>
  <div class="value-art is-blue" style="left:176px;top:373px;width:111px;height:70px" role="img" aria-label="Illustration of people assembling puzzle pieces"></div>

  <div class="value-art is-light" style="left:37px;top:467px;width:122px;height:67px" role="img" aria-label="Illustration of people holding gears around a lightbulb"></div>
  <div class="value" style="left:186px;top:477px">
    <h3>Passion</h3>
    <p>Passion infuses our work with energy, transforming routine tasks into opportunities for creativity and innovation. Fueled by passion, individuals become unstoppable forces, driven to overcome challenges and achieve remarkable outcomes that benefit them and inspire those around them.</p>
  </div>

  <div class="value" style="left:37px;top:571px">
    <h3>Excellence</h3>
    <p>Excellence isn't a destination; it's a continuous journey of refinement and growth. Striving for excellence cultivates a culture of continuous improvement, fostering innovation, credibility, and a lasting impact that resonates far beyond the immediate task.</p>
  </div>
  <div class="value-art is-blue" style="left:175px;top:557px;width:114px;height:68px" role="img" aria-label="Illustration of a clock, target and rising arrow"></div>

  <div class="value-art is-light" style="left:37px;top:649px;width:71px;height:68px" role="img" aria-label="Illustration of a person climbing steps toward a trophy"></div>
  <div class="value" style="left:181px;top:663px">
    <h3>Tenacity</h3>
    <p>Tenacity is the unwavering anchor that keeps us grounded amidst adversity, propelling us forward when faced with obstacles. The resilience to persist, adapt, and learn from setbacks leads to the mastery of skills and the fulfillment of ambitious goals.</p>
  </div>

  <div class="value" style="left:37px;top:751px">
    <h3>Solution Mindset</h3>
    <p>A solution mindset is the compass that directs our focus from problems to possibilities. It empowers us to navigate challenges with a proactive mindset, igniting a journey of exploration and innovation that not only resolves issues but also paves the way for continuous growth and success.</p>
  </div>
  <div class="value-art" style="left:206px;top:741px;width:82px;height:68px" role="img" aria-label="Illustration of people building a lightbulb from puzzle pieces"></div>

  <div class="value-art is-light" style="left:37px;top:831px;width:132px;height:70px" role="img" aria-label="Illustration of people helping each other up steps"></div>
  <div class="value" style="left:186px;top:843px">
    <h3>Generosity</h3>
    <p>Generosity creates a virtuous cycle of goodwill, fostering a sense of unity and shared purpose among colleagues. By freely sharing knowledge, support, and resources, we uplift those around us and contribute to a collaborative environment where collective achievements flourish.</p>
  </div>

  <footer>
    <div class="footer"></div>
    <svg class="footer-wave" width="324" height="62" viewBox="0 0 324 62" aria-hidden="true">
      <path d="M0 0 L324 0 L324 2 C290 8 270 30 240 40 C200 55 160 40 120 42 C90 44 70 56 40 52 C25 50 10 44 0 40 Z" fill="#ffffff"/>
      <path d="M0 0 L40 0 C30 10 10 20 0 26 Z" fill="#ffffff"/>
    </svg>
    <section class="newsletter">
      <h4>Subscribe Our Newsletter</h4>
      <p>Subscribe our newsletter to receive the latest news<br>and exclusive offers every week. No spam.</p>
      <div class="email-field">Enter email address<span class="send"></span></div>
    </section>

    <div class="footer-brand">Altivon</div>
    <div class="socials"><span></span><span></span><span></span><span></span></div>
    <div class="footer-cta">CONTACT US</div>

    <div class="f-col" style="left:133px">
      <h5>Quick links</h5>
      <ul><li>Home</li><li>About Us</li><li>Services</li><li>Insights</li><li>Join Us</li><li>Contact Us</li></ul>
    </div>
    <div class="f-col" style="left:180px">
      <h5>Our Services</h5>
      <ul><li>Business Transformation</li><li>ERP Implementations</li><li>ERP Solutions</li><li>BI and Data</li><li>Building the Right Team…</li></ul>
    </div>
    <div class="f-col" style="left:243px">
      <h5>Contact info</h5>
      <div class="contact-row">Email:<br>hello@altivonconsult.com</div>
      <div class="contact-row">Phone:<br>+44 120 555 0148</div>
      <div class="contact-row">Location:<br>Some address line goes<br>here city name</div>
    </div>
    <div class="copyright">© Altivon Design 2023, All Rights Reserved</div>
    <div class="chat"></div>
  </footer>
</main>

<!-- timeline state: 2020 – 2021 -->
<section class="panel" style="top:36px">
  <div class="skyline" role="img" aria-label="Faint city skyline illustration"></div>
  <div class="chev is-yellow" style="top:37px"><span class="flag"></span>2017 - 2019</div>
  <div class="chev is-steel is-active" style="top:66.5px"><span class="flag"></span>2020 – 2021</div>
  <div class="chev is-sky" style="top:96px"><span class="flag"></span>2022 and Onward</div>
  <h2 class="tl-title" style="left:261px;top:35px">2020 – 2021</h2>
  <div class="tl-line" style="left:273px;top:87px;height:12px"></div>
  <div class="tl-item" style="left:261px;top:63px"><span class="tl-icon"><i></i></span>Pandemic Pauses Growth</div>
  <div class="tl-item" style="left:261px;top:99px;align-items:flex-start"><span class="tl-icon"><i></i></span>Rethinking :</div>
  <ul class="bullets" style="left:300px;top:109px"><li>the business model</li><li>the delivery model</li></ul>
  <div class="vertical" style="left:435px;top:74px">Our Story</div>
</section>

<!-- timeline state: 2022 and Onward -->
<section class="panel" style="top:307px">
  <div class="skyline" role="img" aria-label="Faint city skyline illustration"></div>
  <div class="chev is-yellow" style="top:37px"><span class="flag"></span>2017 - 2019</div>
  <div class="chev is-steel" style="top:66.5px"><span class="flag"></span>2020 - 2021</div>
  <div class="chev is-sky is-active" style="top:96px"><span class="flag"></span>2022 and Onward</div>
  <h2 class="tl-title" style="left:254px;top:35px">2022 and Onward</h2>
  <div class="tl-line" style="left:266px;top:87px;height:49px"></div>
  <div class="tl-item" style="left:254px;top:63px"><span class="tl-icon"><i></i></span>Leadership Team for<br>Focus on Essential Areas</div>
  <div class="tl-item" style="left:254px;top:99px"><span class="tl-icon"><i></i></span>Rapid Growth</div>
  <div class="tl-item" style="left:254px;top:135.5px"><span class="tl-icon"><i></i></span>Customer Success</div>
  <div class="vertical" style="left:435px;top:74px">Our Story</div>
</section>

</body>
</html>
```